TrellBrook and TrellDispatch Business Card

I like a business card design for TrellBrook and TrellDispatch. I like both logo's TrellBrook and TrellDispatch on the card. I like my picture on the card. And here are the information I like on the card:

Trell Brook Technologies
Devin Okafor
CEO

Personal Cell: 604-555-0172
North America Toll Free: 1-866-555-0193
Websites: http://www.trellbrook.example
http://www.trelldispatch.example

Address:
4400 East 19th Ave Suite 2200
Vancouver, BC, V5X 2K9

Web Hosting, Domain Name, and Search Engine Marketing Services.

```html
<!DOCTYPE html>
<html lang="en">
<head>
<meta charset="utf-8">
<title>TrellBrook and TrellDispatch Business Card</title>
<link rel="stylesheet" href="https://fonts.googleapis.com/css2?family=Tinos:wght@400;700&family=Lato:wght@700;900&family=Arimo:wght@400&display=swap">
<style>
  :root {
    --navy: #2a3a82;
    --red: #d3252f;
    --paper: #ffffff;
    --backdrop: #e8e4dd;
    --photo-light: #f2f2f2;
    --photo-mid: #8c8d92;
    --photo-dark: #26272c;
  }
  * { box-sizing: border-box; margin: 0; padding: 0; }
  html, body { width: 1200px; height: 1000px; overflow: hidden; }
  body { background: var(--backdrop); position: relative; font-family: "Arimo", Arial, sans-serif; }

  .card {
    position: absolute;
    background: var(--paper);
    box-shadow: 0 6px 14px rgba(0,0,0,0.25);
    overflow: hidden;
  }

  /* Front card */
  .card--front { left: 111px; top: 65px; width: 700px; height: 410px; }
  .front-services {
    position: absolute; top: 34px; left: 0; width: 100%;
    text-align: center; color: var(--navy);
    font-size: 15px; letter-spacing: 0.4px; word-spacing: 4px;
  }
  .front-brand {
    position: absolute; top: 206px; left: 0; width: 100%;
    text-align: center; color: var(--navy);
    font-family: "Tinos", "Times New Roman", serif;
    font-size: 112px; line-height: 1; letter-spacing: -2px;
  }
  .front-tagline {
    position: absolute; top: 322px; left: 0; width: 100%;
    text-align: center; color: var(--navy);
    font-family: "Tinos", "Times New Roman", serif;
    font-size: 31px; letter-spacing: 0.6px;
  }
  .front-sites {
    position: absolute; top: 382px; left: 0; width: 100%;
    text-align: center; color: var(--navy); font-size: 15px;
  }
  .front-sites .divider { color: var(--red); margin: 0 28px; }
  .accent { color: var(--red); }

  /* Back card */
  .card--back { left: 436px; top: 521px; width: 693px; height: 395px; }
  .edge-stripe { position: absolute; left: 0; top: 0; width: 9px; height: 100%; }
  .edge-stripe__top { height: 50%; background: var(--navy); }
  .edge-stripe__bottom { height: 50%; background: var(--red); }

  .back-brand {
    position: absolute; left: 58px; top: 60px;
    color: var(--navy);
    font-family: "Lato", Arial, sans-serif; font-weight: 900;
    font-size: 25px; line-height: 1;
  }
  .back-brand__sub {
    position: absolute; left: 112px; top: 92px;
    color: var(--navy);
    font-family: "Tinos", "Times New Roman", serif; font-size: 11px;
  }
  .identity {
    position: absolute; left: 54px; top: 122px;
    font-family: "Lato", Arial, sans-serif; font-weight: 700;
    font-size: 21px; line-height: 27px; color: var(--navy);
  }
  .identity__role { color: var(--red); }
  .contact {
    position: absolute; left: 54px; top: 231px;
    color: var(--navy); font-size: 15px; line-height: 20.5px;
    letter-spacing: 0.4px; word-spacing: 3px;
  }
  .address { margin-top: 14px; }
  .portrait {
    position: absolute; right: 0; top: 0; width: 268px; height: 100%;
    background: linear-gradient(180deg, var(--photo-light) 0%, var(--photo-mid) 55%, var(--photo-dark) 100%);
  }
</style>
</head>
<body>
  <section class="card card--front" aria-label="Business card front">
    <p class="front-services">WEB HOSTING, DOMAIN NAME, AND SEARCH ENGINE MARKETING SERVICES</p>
    <p class="front-brand">TrellDispatch</p>
    <p class="front-tagline">SEARCH ENGINE MARKETING SERVICES</p>
    <p class="front-sites">WWW.TRELL<span class="accent">BROOK</span>.EXAMPLE<span class="divider">|</span>WWW.TRELL<span class="accent">DISPATCH</span>.EXAMPLE</p>
  </section>

  <section class="card card--back" aria-label="Business card back">
    <div class="edge-stripe"><div class="edge-stripe__top"></div><div class="edge-stripe__bottom"></div></div>
    <p class="back-brand">TrellBrook</p>
    <p class="back-brand__sub">Web Hosting</p>
    <div class="identity">
      <p>TRELL <span class="accent">BROOK</span> TECHNOLOGIES</p>
      <p>DEVIN OKAFOR</p>
      <p class="identity__role">CEO</p>
    </div>
    <div class="contact">
      <p>PERSONAL CELL: 604-555-0172</p>
      <p>NORTH AMERICA TOLL FREE: 1-866-555-0193</p>
      <p>WWW.TRELL<span class="accent">BROOK</span>.EXAMPLE</p>
      <p>WWW.TRELL<span class="accent">DISPATCH</span>.EXAMPLE</p>
      <div class="address">
        <p>4400 EAST 19TH AVE SUITE 2200</p>
        <p>VANCOUVER, BC, V5X 2K9</p>
      </div>
    </div>
    <div class="portrait" role="img" aria-label="Portrait photo of the CEO"></div>
  </section>
</body>
</html>
```